Business Card Design Quandong Celebration Crafters

on the front i would like to see the logo and my contact details. on the back i would like it to include the 3 parts to the business party planning, party hire and party supplies also with a line at the bottom (or white space) to write their appointment details.

Target Market(s)

mums and corporates

Industry/Entity Type

Business

Requirements
Must have
• logo and contact details which are: Name: Rosalind, Phone: 0417365920, email: ros@quandongfetes.com.au, Website: www.quandongfetes.com.au,

```html
<!DOCTYPE html>
<html lang="en">
<head>
<meta charset="utf-8">
<title>Quandong Celebration Crafters – Business Cards</title>
<link rel="stylesheet" href="https://fonts.googleapis.com/css2?family=Open+Sans:wght@400;600;800&family=Pacifico&family=Titan+One&display=swap">
<style>
  :root {
    --page: #eef1f3;
    --card-deep: #1596c4;
    --card-mid: #23b2dc;
    --card-light: #6fd0ee;
    --bubble: #ffffff;
    --bubble-shade: #e6ecef;
    --ink: #3a4a55;
    --name-blue: #1a9fd6;
    --pink: #ec3f8f;
    --yellow: #ffd21f;
    --sky: #4cc3f0;
    --outline: #1b2330;
    --brand: #ffffff;
    --art-warm: #e9a3b6;
    --art-cool: #9fb6e6;
  }
  * { box-sizing: border-box; margin: 0; padding: 0; }
  html, body { width: 1200px; height: 805px; overflow: hidden; background: var(--page); }
  body { font-family: "Open Sans", sans-serif; }

  .sheet {
    width: 1200px; height: 805px;
    display: flex; align-items: center; justify-content: center; gap: 40px;
  }
  .card {
    position: relative;
    width: 540px; height: 318px;
    border-radius: 22px;
    overflow: hidden;
    background: radial-gradient(circle at 30% 62%, var(--card-light) 0%, var(--card-mid) 42%, var(--card-deep) 100%);
    box-shadow: 0 10px 28px rgba(20, 60, 80, .25);
  }

  /* brand block */
  .brand {
    position: absolute; left: 34px; top: 150px;
    display: flex; align-items: center; gap: 12px;
  }
  .brand-art {
    width: 58px; height: 58px; border-radius: 50%;
    background: linear-gradient(160deg, var(--art-warm), var(--art-cool));
    flex: none;
  }
  .brand-name {
    font-family: "Open Sans", sans-serif; font-weight: 800;
    color: var(--brand);
    font-size: 19px; line-height: 1.12;
    width: 150px;
  }

  /* back side */
  .services {
    position: absolute; left: 248px; top: 38px;
    list-style: none;
    font-family: "Titan One", sans-serif;
    font-size: 19px; line-height: 1.75;
    -webkit-text-stroke: 1px var(--outline);
    paint-order: stroke fill;
  }
  .service--planning { color: var(--pink); }
  .service--hire { color: var(--yellow); }
  .service--supplies { color: var(--sky); }
  .balloons {
    position: absolute; width: 38px; height: 34px;
    border-radius: 8px;
    background: linear-gradient(135deg, var(--art-warm), var(--art-cool));
  }
  .balloons--side { left: 200px; top: 40px; }
  .balloons--top { left: 478px; top: 18px; }
  .appointment {
    position: absolute; left: 44px; right: 30px; bottom: 26px;
    height: 46px;
  }

  /* front side */
  .contact-bubble {
    position: absolute; right: 22px; top: 20px;
    width: 360px; height: 180px;
  }
  .bubble-shape { position: absolute; left: 0; top: 0; }
  .contact-body {
    position: absolute; left: 0; top: 0; width: 360px; height: 166px;
    padding: 18px 26px;
  }
  .contact-name {
    font-family: "Pacifico", cursive; font-weight: 400;
    color: var(--name-blue);
    font-size: 34px; line-height: 1.1;
    margin-bottom: 12px;
  }
  .contact-list { list-style: none; color: var(--ink); font-size: 13.5px; }
  .contact-list li {
    display: flex; align-items: center; gap: 12px;
    padding: 5px 0;
    border-top: 1px solid var(--bubble-shade);
  }
  .contact-list svg { width: 16px; height: 16px; flex: none; }
  .card--front .brand { top: 214px; }
</style>
</head>
<body>
<main class="sheet">

  <section class="card card--back" aria-label="Card back">
    <div class="balloons balloons--top" role="img" aria-label="Small bunch of party balloons"></div>
    <div class="balloons balloons--side" role="img" aria-label="Small bunch of party balloons"></div>
    <ul class="services">
      <li class="service--planning">Business party planning</li>
      <li class="service--hire">Party hire</li>
      <li class="service--supplies">Party supplies</li>
    </ul>
    <div class="brand">
      <span class="brand-art" role="img" aria-label="Mascot holding party balloons"></span>
      <span class="brand-name">Quandong Celebration Crafters</span>
    </div>
    <svg class="appointment" viewBox="0 0 466 46" preserveAspectRatio="none" role="img" aria-label="Space to write appointment details">
      <rect x="0" y="0" width="466" height="40" rx="20" fill="#ffffff"/>
      <path d="M14 36 L4 46 L28 38 Z" fill="#ffffff"/>
    </svg>
  </section>

  <section class="card card--front" aria-label="Card front">
    <div class="contact-bubble">
      <svg class="bubble-shape" width="360" height="180" viewBox="0 0 360 180" aria-hidden="true">
        <rect x="0" y="0" width="360" height="166" rx="6" fill="#ffffff"/>
        <path d="M22 164 L18 180 L40 164 Z" fill="#ffffff"/>
      </svg>
      <div class="contact-body">
        <h1 class="contact-name">Rosalind</h1>
        <ul class="contact-list">
          <li>
            <svg viewBox="0 0 16 16" aria-hidden="true"><rect x="4" y="1.5" width="8" height="13" rx="1.5" fill="none" stroke="#1a9fd6" stroke-width="1.4"/><circle cx="8" cy="12" r=".9" fill="#1a9fd6"/></svg>
            <span>0417365920</span>
          </li>
          <li>
            <svg viewBox="0 0 16 16" aria-hidden="true"><rect x="1.5" y="3.5" width="13" height="9" rx="1" fill="none" stroke="#1a9fd6" stroke-width="1.4"/><path d="M1.5 4 L8 9 L14.5 4" fill="none" stroke="#1a9fd6" stroke-width="1.4"/></svg>
            <span>ros@quandongfetes.com.au</span>
          </li>
          <li>
            <svg viewBox="0 0 16 16" aria-hidden="true"><circle cx="8" cy="8" r="6.5" fill="#1a9fd6"/><path d="M1.5 8 H14.5 M8 1.5 C5 5 5 11 8 14.5 M8 1.5 C11 5 11 11 8 14.5" fill="none" stroke="#fff" stroke-width="1"/></svg>
            <span>www.quandongfetes.com.au</span>
          </li>
        </ul>
      </div>
    </div>
    <div class="brand">
      <span class="brand-art" role="img" aria-label="Mascot holding party balloons"></span>
      <span class="brand-name">Quandong Celebration Crafters</span>
    </div>
  </section>

</main>
</body>
</html>
```